PDN Letterhead

We need a letterhead design that will be able to be used on all marketing products (letterhead, mail chimp, envelops, business cards, etc.) We are a law firm specializing primarily in transportation law but offer a wide range of services to our clients. We would like the design to be modern, simple, and professional. Our colors are black and gold, however, we've incorporated dark gray and white on other marketing products such as our website.

```html
<!DOCTYPE html>
<html lang="en">
<head>
<meta charset="utf-8">
<title>PDN Envelope</title>
<link rel="stylesheet" href="https://fonts.googleapis.com/css2?family=Cinzel:wght@400;500&display=swap">
<style>
  :root{
    --gold:#a88a5c;
    --gold-dark:#96784b;
    --black:#121212;
    --ink:#1c1c1c;
    --paper:#fbfbfa;
    --backdrop:#e8e5e0;
  }
  *{margin:0;padding:0;box-sizing:border-box}
  html,body{width:1200px;height:960px;overflow:hidden;background:var(--backdrop)}
  .envelope{
    position:absolute;left:80px;top:212px;width:1040px;height:535px;
    background:var(--paper);overflow:hidden;
    box-shadow:0 2px 10px rgba(0,0,0,.12);
  }
  .envelope-shapes{position:absolute;inset:0}
  .firm-name{
    position:absolute;left:36px;top:148px;
    font-family:"Cinzel",serif;font-weight:500;color:var(--black);
    line-height:1;
  }
  .firm-name .primary{display:block;font-size:50px;letter-spacing:1px}
  .firm-name .secondary{display:block;font-size:24px;letter-spacing:5px;margin-top:12px;padding-left:10px}
  .contact{
    position:absolute;left:38px;top:285px;list-style:none;
    font-family:"Cinzel",serif;font-size:19px;color:var(--ink);
  }
  .contact li{display:flex;align-items:flex-start;height:33px}
  .contact svg{width:14px;height:14px;margin:4px 12px 0 0;fill:var(--gold);flex:none}
  .contact .address{line-height:23px;height:auto}
</style>
</head>
<body>
<div class="envelope">
  <svg class="envelope-shapes" viewBox="0 0 1040 535" aria-hidden="true">
    <polygon points="0,0 1040,0 980,78 60,78" fill="var(--gold)"/>
    <polygon points="0,0 42,0 0,78" fill="var(--black)"/>
    <polygon points="0,100 0,88 52,0 64,0" fill="var(--gold)"/>
    <polygon points="636,535 1040,384 1040,402 660,535" fill="var(--gold)"/>
    <polygon points="660,535 1040,414 1040,535" fill="var(--black)"/>
  </svg>

  <div class="firm-name">
    <span class="primary">PENDAN</span>
    <span class="secondary">LAW GROUP</span>
  </div>

  <ul class="contact">
    <li><svg viewBox="0 0 16 16"><path d="M3 1l3 3-1.5 2a9 9 0 0 0 5.5 5.5L12 10l3 3-2 2C7 15 1 9 1 3z"/></svg>555.010.2040</li>
    <li><svg viewBox="0 0 16 16"><path d="M1 3h14v10H1zM2 4l6 5 6-5" stroke="var(--paper)" stroke-width="1.2"/></svg>ADMIN@PENDANLAWGROUP.COM</li>
    <li><svg viewBox="0 0 16 16"><circle cx="8" cy="8" r="7"/><path d="M1 8h14M8 1c-3 4-3 10 0 14M8 1c3 4 3 10 0 14" stroke="var(--paper)" stroke-width="1" fill="none"/></svg>WWW.PENDANLAWGROUP.COM</li>
    <li class="address"><svg viewBox="0 0 16 16"><path d="M8 0a5.5 5.5 0 0 0-5.5 5.5C2.5 10 8 16 8 16s5.5-6 5.5-10.5A5.5 5.5 0 0 0 8 0zm0 8a2.5 2.5 0 1 1 0-5 2.5 2.5 0 0 1 0 5z"/></svg><span>740 West Harbor Avenue,<br>Suite 210</span></li>
  </ul>
</div>
</body>
</html>
```